Creative Businesss Card desgin!

Create a business card for our business Gleam window cleaning!
We are open to creative ideas as long as it maintains a professional image.

Target Market(s)

Small Commercial window cleaning clients including car dealerships, strata manager, cafe

Industry/Entity Type

Window Cleaning

Contact Information for Business Card

Daniel Prescott
General Manager
Gleam Window Cleaning

daniel@gleamservices.com.au
pane-care-southbank.com.au
Ph: 1800 GET GLEAM
Mob: 0437 582 061

Colors
fbed22
0392cd

Requirements
Should not have
• Stock window cleaning/ squeegee graphics

```html
<!DOCTYPE html>
<html lang="en">
<head>
<meta charset="utf-8">
<title>Gleam Window Cleaning – Business Card</title>
<link rel="stylesheet" href="https://fonts.googleapis.com/css2?family=Montserrat:wght@800&family=PT+Sans:wght@400;700&display=swap">
<style>
  :root {
    --stage: #2b2e33;
    --blue: #0b5e98;
    --yellow: #f5ec1f;
    --yellow-deep: #ecd81a;
    --navy: #0d2a44;
    --white: #ffffff;
  }
  * { box-sizing: border-box; margin: 0; padding: 0; }
  html, body {
    width: 1200px; height: 900px; overflow: hidden;
    background: var(--stage);
  }
  .canvas {
    width: 1200px; height: 900px;
    display: flex; flex-direction: column;
    align-items: center; justify-content: center; gap: 70px;
  }
  .card {
    position: relative;
    width: 600px; height: 343px;
    border-radius: 22px;
    overflow: hidden;
    background: var(--blue);
    box-shadow: 0 10px 30px rgba(0,0,0,.35);
  }
  .card-shapes { position: absolute; inset: 0; }

  /* Front */
  .brand { position: absolute; left: 40px; top: 30px; color: var(--yellow);
           font-family: "Montserrat", sans-serif; font-weight: 800; text-transform: uppercase; }
  .brand-name { display: block; font-size: 70px; line-height: 1; letter-spacing: 2px; }
  .brand-tagline { display: block; font-size: 19px; letter-spacing: 1px; margin-top: 4px; }
  .person { position: absolute; left: 40px; top: 145px; font-family: "PT Sans", sans-serif; }
  .person-name { color: var(--yellow); font-size: 24px; font-weight: 700; line-height: 1.1; }
  .person-title { color: var(--white); font-size: 14px; }
  .contacts { position: absolute; left: 30px; top: 218px; list-style: none;
              font-family: "PT Sans", sans-serif; color: var(--navy); font-size: 17px; }
  .contacts li { display: flex; align-items: center; height: 27px; }
  .contact-icon { width: 28px; display: flex; justify-content: center; margin-right: 14px; }
  .contact-icon svg { width: 15px; height: 15px; }

  /* Back */
  .brand-centered { left: 0; right: 0; top: 105px; text-align: center; }
  .brand-centered .brand-name { font-size: 96px; letter-spacing: 4px; }
  .brand-centered .brand-tagline { font-size: 26px; letter-spacing: 2px; margin-top: 6px; }
</style>
</head>
<body>
<main class="canvas">

  <section class="card card-front" aria-label="Business card front">
    <svg class="card-shapes" viewBox="0 0 600 343" aria-hidden="true">
      <polygon points="0,205 440,205 520,343 0,343" fill="var(--yellow)"/>
      <rect x="30" y="205" width="28" height="138" fill="var(--yellow-deep)"/>
    </svg>
    <div class="brand">
      <span class="brand-name">Gleam</span>
      <span class="brand-tagline">Window Cleaning</span>
    </div>
    <div class="person">
      <p class="person-name">Daniel Prescott</p>
      <p class="person-title">General Manager</p>
    </div>
    <ul class="contacts">
      <li><span class="contact-icon"><svg viewBox="0 0 16 16"><path d="M4 1.5l2.5 3-1.5 1.5c.8 1.8 2.2 3.2 4 4l1.5-1.5 3 2.5-1.5 2.5C7 13 3 9 1.5 3z" fill="var(--navy)"/></svg></span>1800 GET GLEAM</li>
      <li><span class="contact-icon"><svg viewBox="0 0 16 16"><rect x="4" y="1" width="8" height="14" rx="1.5" fill="none" stroke="var(--navy)" stroke-width="1.5"/><circle cx="8" cy="12.5" r="0.9" fill="var(--navy)"/></svg></span>0437 582 061</li>
      <li><span class="contact-icon"><svg viewBox="0 0 16 16"><rect x="1" y="3.5" width="14" height="9" fill="var(--navy)"/><path d="M1 3.5l7 5.5 7-5.5" fill="none" stroke="var(--yellow)" stroke-width="1.2"/></svg></span>daniel@gleamservices.com.au</li>
      <li><span class="contact-icon"><svg viewBox="0 0 16 16"><g fill="none" stroke="var(--navy)" stroke-width="1.3"><circle cx="8" cy="8" r="6.5"/><ellipse cx="8" cy="8" rx="3" ry="6.5"/><path d="M1.5 8h13M2.5 5h11M2.5 11h11"/></g></svg></span>pane-care-southbank.com.au</li>
    </ul>
  </section>

  <section class="card card-back" aria-label="Business card back">
    <svg class="card-shapes" viewBox="0 0 600 343" aria-hidden="true">
      <polygon points="245,0 345,0 295,55" fill="var(--yellow)"/>
      <polygon points="300,283 255,343 345,343" fill="var(--yellow)"/>
    </svg>
    <div class="brand brand-centered">
      <span class="brand-name">Gleam</span>
      <span class="brand-tagline">Window Cleaning</span>
    </div>
  </section>

</main>
</body>
</html>
```